Exciting Personal Development Book Cover: FIND ZEN NOW!

Design a Book Cover for my personal development book.
Title: Find Zen Now!
Author: Marcus Telly
Tagline: A real-life solution to get unstuck and break free

My picture must make up the front cover as I need to build my brand and people should recognise me on book shelves. Bold and catchy. How you do it is up to you. There must be space for a short testimonial from a famous person who is currently reading my book. I uploaded a sample of what I made in Photoshop but I don't have design skills.

I've added a PDF of my book so you can read the chapter index and introduction to get a sense of the content.

Target Market(s)

Personal Development Self-Help Market

Industry/Entity Type

Personal Development

Font styles to use
Serif
Sans Serif

Requirements
Must have
• My picture as hero image on cover.
Nice to have
• Must have Title, Tagline and my author name. If possible ZEN stands for 'Zeal, Energy & Nerve' If there is a way to fit this somewhere great. If it's too much then it can go somewhere on the back.

```html
<!DOCTYPE html>
<html lang="en">
<head>
<meta charset="UTF-8">
<title>Find Zen Now! – Book Cover</title>
<link rel="stylesheet" href="https://fonts.googleapis.com/css2?family=Saira+Extra+Condensed:wght@500&family=Lexend:wght@300;600&display=swap">
<style>
  :root {
    --backdrop: #e0e0e0;
    --cover: #131313;
    --spine: #1a1a1a;
    --spine-line: #0c0c0c;
    --light: #f2f2f2;
    --ink: #1c1c1c;
    --author-ink: #4a4a4a;
    --photo-hi: #9a9a9a;
    --photo-mid: #4a4a4a;
  }
  * { margin: 0; padding: 0; box-sizing: border-box; }
  html, body {
    width: 1200px;
    height: 800px;
    overflow: hidden;
    background: var(--backdrop);
  }
  .cover {
    position: absolute;
    left: 334px;
    top: 30px;
    width: 531px;
    height: 740px;
    background: var(--cover);
    overflow: hidden;
  }
  .spine-fold {
    position: absolute;
    left: 0; top: 0;
    width: 38px; height: 100%;
    background: var(--spine);
    border-right: 2px solid var(--spine-line);
  }
  .author-photo {
    position: absolute;
    left: 234px;
    top: 41px;
    width: 297px;
    height: 660px;
    background:
      radial-gradient(ellipse 60% 22% at 62% 22%, var(--photo-hi), transparent 70%),
      radial-gradient(ellipse 70% 45% at 65% 62%, var(--photo-hi), var(--photo-mid) 55%, transparent 85%);
  }
  .meaning-band {
    position: absolute;
    left: 0;
    top: 102px;
    width: 71px;
    height: 370px;
    background: var(--light);
  }
  .meaning-band span {
    position: absolute;
    top: 0;
    right: 6px;
    height: 100%;
    writing-mode: vertical-rl;
    font-family: "Lexend", sans-serif;
    font-weight: 300;
    font-size: 28px;
    line-height: 30px;
    color: var(--ink);
    text-align: center;
    white-space: nowrap;
  }
  .title {
    position: absolute;
    left: 84px;
    top: 75px;
    font-family: "Saira Extra Condensed", sans-serif;
    font-weight: 500;
    font-size: 146px;
    line-height: 135px;
    color: var(--light);
    letter-spacing: 1px;
  }
  .title span { display: block; }
  .tagline {
    position: absolute;
    left: 38px;
    top: 563px;
    font-family: "Lexend", sans-serif;
    font-weight: 300;
    font-size: 19px;
    line-height: 26px;
    color: var(--light);
    letter-spacing: 0.6px;
  }
  .tagline strong { font-weight: 600; }
  .author-name {
    position: absolute;
    left: 195px;
    bottom: 0;
    width: 141px;
    height: 28px;
    background: var(--light);
    font-family: "Lexend", sans-serif;
    font-weight: 600;
    font-size: 15px;
    line-height: 28px;
    text-align: center;
    color: var(--author-ink);
  }
</style>
</head>
<body>
  <main class="cover">
    <div class="spine-fold"></div>
    <div class="author-photo" role="img" aria-label="Black and white portrait of the author smiling, in a white shirt with tattooed forearms"></div>
    <div class="meaning-band"><span>Zeal, Energy &amp; Nerve</span></div>
    <h1 class="title"><span>Find</span><span>ZEN</span><span>Now!</span></h1>
    <p class="tagline">A real-life solution to get<br><strong>unstuck</strong> and <strong>break free</strong></p>
    <p class="author-name">Marcus Telly</p>
  </main>
</body>
</html>
```